cover design for presentation folder

I am looking for a simple cover design for a 9X12 folder cover. I want our logo featured and some design element from our logo incorporated. I have attached two versions on our logo.

Colors

Designer to choose colors to be used in the design.

```html
<!DOCTYPE html>
<html lang="en">
<head>
<meta charset="utf-8">
<title>Presentation Folder Cover</title>
<link rel="stylesheet" href="https://fonts.googleapis.com/css2?family=Open+Sans:wght@700&display=swap">
<style>
  :root {
    --backdrop: #d6d6d6;
    --paper: #ffffff;
    --green-deep: #066b38;
    --green: #0f7d42;
    --green-light: #23924a;
    --gold: #fbb018;
    --navy: #2e3192;
  }
  html, body {
    margin: 0;
    padding: 0;
    width: 1200px;
    height: 847px;
    overflow: hidden;
    background: var(--backdrop);
  }
  .folder-spread {
    position: absolute;
    left: 60px;
    top: 63px;
    width: 1080px;
    height: 720px;
    background: var(--paper);
    box-shadow: 0 12px 30px rgba(0, 0, 0, 0.25);
    overflow: hidden;
  }
  .folder-art {
    position: absolute;
    inset: 0;
    width: 100%;
    height: 100%;
    display: block;
  }
  .brand-lockup {
    position: absolute;
    left: 760px;
    top: 520px;
    display: flex;
    align-items: center;
    gap: 14px;
  }
  .brand-square {
    width: 56px;
    height: 56px;
    background: var(--navy);
  }
  .brand-name {
    margin: 0;
    font-family: "Open Sans", sans-serif;
    font-weight: 700;
    font-size: 22px;
    line-height: 1.15;
    letter-spacing: 0.5px;
    text-transform: uppercase;
    color: var(--navy);
    white-space: nowrap;
  }
</style>
</head>
<body>
  <div class="folder-spread">
    <svg class="folder-art" viewBox="0 0 1080 720" aria-hidden="true">
      <defs>
        <linearGradient id="back-tone" x1="0" y1="0" x2="1" y2="0">
          <stop offset="0" stop-color="var(--green-deep)"/>
          <stop offset="1" stop-color="var(--green)"/>
        </linearGradient>
      </defs>
      <rect class="back-panel" x="0" y="0" width="540" height="720" fill="url(#back-tone)"/>
      <path class="front-sweep" d="M540,0 H760 Q700,320 540,600 Z" fill="var(--green-light)"/>
      <path class="front-rule" d="M772,0 Q712,330 540,624" fill="none" stroke="var(--gold)" stroke-width="10"/>
      <line class="back-rule" x1="0" y1="660" x2="540" y2="660" stroke="var(--gold)" stroke-width="10"/>
      <line class="spine" x1="540" y1="0" x2="540" y2="720" stroke="rgba(0,0,0,0.08)" stroke-width="1"/>
    </svg>

    <div class="brand-lockup">
      <div class="brand-square"></div>
      <p class="brand-name">Highland Valley<br>Community Fund</p>
    </div>
  </div>
</body>
</html>
```